Spiritual journeyer, astrologer, Reiki master, underground music lover needs business card design

Initially I need a business card design (and possibly a logo for my new website). I offer astrological and energetic inquiry and guidance to clients in support of their life's evolutionary path. I combine an eclectic mix of methods with a focus on the mind body connection. I am a spiritual journeyer, astrologer, Reiki Master, certified personal trainer, soon to be black belt in Taekwondo (karate), and researcher into the benefits of music/sound vibrational therapy. And underground music lover :) The attached drawing is just something I drew freehand, it is symbolic of many things important to me. I wanted the figure to clearly be female. Her arms are open to catch the sky, the name of my new business is Orlabrook, and Orla is my daughter's name. This was just an idea I had, I'm open to suggestions. The photo is me with the planets in the sky as they were at the moment I was born (some years ago-LOL)
Updates

I have picked a final design. Thank you everyone for your time and effort.

Target Market(s)

Worldwide, what I do can be done in person or anywhere in the world via Skype

Industry/Entity Type

Professional Service

Contact Information for Business Card

Simple, unusual image with my business name and contact info

Font styles to use
Sans Serif

Requirements
Must have
• My website very clean, simple. Somehow combine biz name of Orlabrook with female figure catching/holding the starry sky? See my poor drawing I attached.
Nice to have
• Something that conveys all the unique, unusual, eclectic skills and capacities I have
Should not have
• Frilly, fancy, stuffy

```html
<!DOCTYPE html>
<html lang="en">
<head>
<meta charset="utf-8">
<title>Orlabrook business cards</title>
<link href="https://fonts.googleapis.com/css2?family=Marcellus&family=Open+Sans:wght@300;400&display=swap" rel="stylesheet">
<style>
  :root {
    --backdrop: #e6e7e9;
    --night: #2a2d5c;
    --indigo: #3b3a86;
    --violet: #6a3d8f;
    --magenta: #c04a86;
    --rose: #d9587e;
    --ink-light: #f3eef6;
    --ink-soft: #d9d3e6;
    --logo-silver: #e4e4ea;
  }
  * { margin: 0; padding: 0; box-sizing: border-box; }
  html, body { width: 1200px; height: 1000px; overflow: hidden; }
  body { background: var(--backdrop); position: relative; font-family: "Open Sans", sans-serif; }

  .card { position: absolute; overflow: hidden; color: var(--ink-light); }
  .card--portrait {
    left: 172px; top: 239px; width: 287px; height: 502px;
    background:
      radial-gradient(ellipse 60% 30% at 30% 12%, rgba(217,88,126,.75), transparent 70%),
      radial-gradient(ellipse 55% 25% at 85% 30%, rgba(192,74,134,.6), transparent 70%),
      radial-gradient(ellipse 70% 30% at 50% 52%, rgba(106,61,143,.55), transparent 70%),
      linear-gradient(180deg, var(--magenta) 0%, var(--violet) 20%, var(--indigo) 45%, var(--night) 75%, #262a52 100%);
  }
  .card--landscape {
    left: 527px; top: 347px; width: 501px; height: 286px;
    background:
      radial-gradient(ellipse 45% 60% at 85% 40%, rgba(217,88,126,.9), transparent 70%),
      radial-gradient(ellipse 40% 50% at 55% 15%, rgba(192,74,134,.65), transparent 70%),
      radial-gradient(ellipse 40% 60% at 10% 80%, rgba(59,58,134,.8), transparent 70%),
      linear-gradient(100deg, var(--night) 0%, var(--indigo) 30%, var(--violet) 55%, var(--magenta) 80%, var(--rose) 100%);
  }

  .brand-name {
    position: absolute;
    font-family: "Marcellus", serif;
    color: var(--logo-silver);
    letter-spacing: .5px;
    line-height: 1;
  }
  .card--portrait .brand-name { left: 0; right: 0; text-align: center; top: 42px; font-size: 29px; }
  .card--landscape .brand-name { left: 23px; top: 25px; font-size: 27px; }

  .portrait-wheel {
    position: absolute; border-radius: 50%;
    background: radial-gradient(circle, #5a4ea6 0%, #3e3f8e 45%, rgba(42,45,92,.85) 80%, rgba(42,45,92,0) 100%);
  }
  .card--portrait .portrait-wheel { left: 31px; top: 93px; width: 226px; height: 226px; }
  .card--landscape .portrait-wheel { left: 38px; top: 48px; width: 210px; height: 210px; }

  .tagline {
    position: absolute; font-weight: 300; font-size: 10.5px;
    letter-spacing: 1.3px; text-transform: uppercase; line-height: 15px; color: var(--ink-soft);
  }
  .card--portrait .tagline { left: 0; right: 0; top: 332px; text-align: center; }
  .card--landscape .tagline { right: 12px; top: 80px; text-align: right; }

  .name-band {
    position: absolute; left: 0; right: 0; top: 380px; height: 26px;
    background: linear-gradient(90deg, rgba(106,61,143,.9), rgba(140,70,170,.85) 40%, rgba(192,74,134,.6) 70%, rgba(106,61,143,.5));
  }
  .name-band--thin { top: 372px; height: 3px; background: rgba(150,110,200,.5); }
  .name-band--lower { top: 414px; height: 4px; background: rgba(150,110,200,.45); }

  .person-name {
    position: absolute; font-family: "Marcellus", serif; text-transform: uppercase; color: #fff; line-height: 1;
  }
  .card--portrait .person-name { left: 0; right: 0; top: 384px; text-align: center; font-size: 20px; }
  .card--landscape .person-name { right: 12px; top: 142px; font-size: 21px; letter-spacing: .3px; }

  .contact { position: absolute; list-style: none; font-size: 13px; letter-spacing: .8px; line-height: 20px; color: var(--ink-soft); }
  .card--portrait .contact { left: 0; right: 0; top: 428px; text-align: center; }
  .card--landscape .contact { right: 12px; top: 174px; text-align: right; color: var(--ink-light); }
</style>
</head>
<body>
  <section class="card card--portrait" aria-label="Portrait business card">
    <div class="brand-name">ORLABROOK</div>
    <div class="portrait-wheel" role="img" aria-label="Photo of a woman seated in meditation with chakra points, over a zodiac birth-chart wheel"></div>
    <p class="tagline">Astrological and energetic<br>guidance and inquiry</p>
    <div class="name-band name-band--thin"></div>
    <div class="name-band"></div>
    <div class="name-band name-band--lower"></div>
    <h1 class="person-name">Maren Ashvale</h1>
    <ul class="contact">
      <li>WWW.ORLABROOK.COM</li>
      <li>EMAIL@ORLABROOK</li>
      <li>555-013-2740</li>
    </ul>
  </section>

  <section class="card card--landscape" aria-label="Landscape business card">
    <div class="brand-name">ORLABROOK</div>
    <div class="portrait-wheel" role="img" aria-label="Photo of a woman seated in meditation with chakra points, over a zodiac birth-chart wheel"></div>
    <p class="tagline">Astrological and energetic<br>guidance and inquiry</p>
    <h2 class="person-name">Maren Ashvale</h2>
    <ul class="contact">
      <li>WWW.ORLABROOK.COM</li>
      <li>EMAIL@ORLABROOK</li>
      <li>555-013-2740</li>
    </ul>
  </section>
</body>
</html>
```